依頼詳細
以前こちらで作成して頂いた雰囲気の内容でお願いします。
※添付チラシ

記載項目
・もえぎうたのロゴマークを入れてください。
https://moegiuta.or.jp/event-t/2020-03-14-2 このアドレス用のQRコードを記載してください。
・添付しました画像を使用してください。
サイズ
A4
ページ数
片面
希望イメージ
シンプル 複雑
単色 カラフル
暗い 明るい
日常 高級
遊び心 厳粛
未来的 伝統的
女性的 男性的
希望する色
納品ファイル
補足説明
■ 選んだ理由

ご提案いただきありがとうございました。
どれも良いご提案で悩みましたが、色合いや、雰囲気、読みやすさ、
これから家づくりを考える対象年齢層などを考慮して
選択させて頂きました。

■ 提案者全員のお礼・コメント

多くのご提案を頂きありがとうございました。<m(__)m>

```html
<!DOCTYPE html>
<html lang="ja">
<head>
<meta charset="utf-8">
<title>「家づくり」はじめの一歩 セミナー</title>
<link href="https://fonts.googleapis.com/css2?family=Noto+Sans+JP:wght@400;700;900&family=Zen+Maru+Gothic:wght@500;700;900&display=swap" rel="stylesheet">
<style>
:root{
  --red:#c8323a;
  --deep-red:#9e2530;
  --pink:#f3a9a6;
  --pale-pink:#fde8e4;
  --orange:#f08a3c;
  --green:#7fae4a;
  --pale-green:#e6f0d6;
  --cream:#fffaf3;
  --ink:#3b3330;
  --muted:#6d6460;
}
*{margin:0;padding:0;box-sizing:border-box}
html,body{width:848px;height:1200px;overflow:hidden;background:#fff}
body{font-family:"Noto Sans JP",sans-serif;color:var(--ink)}
.flyer{position:relative;width:848px;height:1200px;background:var(--cream);overflow:hidden}

.hero-photo{position:absolute;left:400px;top:0;width:448px;height:270px;
  background:linear-gradient(135deg,#eef1f4 0%,#f7f3ee 45%,#e9e2d8 100%)}
.hero-fade{position:absolute;left:0;top:0;width:848px;height:300px;
  background:linear-gradient(180deg,rgba(255,250,243,0) 65%,var(--cream) 100%)}

.brand-box{position:absolute;left:14px;top:10px;width:116px;height:100px;border:3px solid var(--green);
  border-radius:14px;background:#fff;display:flex;flex-direction:column;align-items:center;justify-content:center;gap:6px}
.brand-dot{width:34px;height:34px;border-radius:50%;background:var(--green)}
.brand-name{font-family:"Zen Maru Gothic",sans-serif;font-weight:700;font-size:17px;color:var(--green)}

.bubble{position:absolute;left:270px;top:14px;padding:6px 16px;background:#fff;border:2px solid var(--orange);
  border-radius:18px;font-family:"Zen Maru Gothic",sans-serif;font-weight:700;font-size:16px;color:var(--orange)}
.url-tag{position:absolute;left:270px;top:52px;font-size:10px;color:var(--muted)}

.seminar-tag{position:absolute;right:12px;top:0;width:230px;height:72px;background:var(--deep-red);color:#fff;
  text-align:center;padding-top:8px;border-radius:0 0 10px 10px;white-space:nowrap}
.seminar-tag small{display:block;font-size:13px;letter-spacing:.2em}
.seminar-tag strong{font-family:"Zen Maru Gothic",sans-serif;font-size:22px;font-weight:900}

.intro{position:absolute;left:22px;top:140px;width:240px;font-size:12.5px;line-height:1.85;color:var(--ink)}
.intro p+p{margin-top:14px}
.intro .accent{color:var(--red);font-weight:700}

.family-art{position:absolute;left:283px;top:150px;width:170px;height:200px;border-radius:20px;
  background:radial-gradient(circle at 50% 45%,#fde3d4 0%,#fbd9c8 45%,rgba(255,250,243,0) 75%)}

.badge{position:absolute;top:360px;width:92px;height:92px;border-radius:50%;color:#fff;
  display:flex;flex-direction:column;align-items:center;justify-content:center;
  font-family:"Zen Maru Gothic",sans-serif;font-weight:900;line-height:1.25;text-align:center}
.badge-kids{left:300px;background:var(--orange);font-size:15px}
.badge-free{left:400px;background:var(--pink);font-size:15px}
.badge-free b{font-size:20px}

.title{position:absolute;left:758px;top:250px;writing-mode:vertical-rl;font-family:"Zen Maru Gothic",sans-serif;
  font-weight:900;font-size:64px;color:var(--red);line-height:1.1;white-space:nowrap}
.subtitle{position:absolute;left:716px;top:300px;writing-mode:vertical-rl;font-family:"Zen Maru Gothic",sans-serif;
  font-weight:700;font-size:25px;color:var(--red);line-height:1.3;white-space:nowrap}

.points{position:absolute;left:582px;top:300px;height:290px;writing-mode:vertical-rl;font-size:13px;
  line-height:1.4;font-weight:700;color:var(--ink)}
.points .lead{color:var(--red)}
.points li{list-style:none;white-space:nowrap}
.points li::before{content:"●";color:var(--orange);font-size:9px;margin-bottom:3px}

.promise{position:absolute;left:14px;top:700px;width:530px;padding:12px 16px;background:var(--pale-pink);
  border-radius:12px;font-family:"Zen Maru Gothic",sans-serif;font-weight:700;font-size:15px;line-height:1.6;color:var(--deep-red);white-space:nowrap}
.promise em{font-style:normal;font-size:21px;color:var(--red)}

.details{position:absolute;left:22px;top:800px;width:520px;font-size:14px}
.details dl{display:grid;grid-template-columns:96px 1fr;column-gap:10px;row-gap:8px;align-items:center}
.details dt{background:var(--red);color:#fff;font-weight:700;text-align:center;border-radius:4px;padding:2px 0;font-size:13px}
.details dd{font-weight:700;white-space:nowrap}
.details dd small{font-weight:400;font-size:11px;color:var(--muted)}

.date-box{position:absolute;left:556px;top:780px;width:192px;height:190px;border:3px solid var(--red);border-radius:10px;
  background:#fff;text-align:center;color:var(--red);overflow:hidden}
.date-box .label{background:var(--red);color:#fff;font-weight:700;font-size:15px;padding:4px 0;letter-spacing:.3em}
.date-box .year{font-size:17px;font-weight:700;margin-top:4px}
.date-box .day{font-family:"Zen Maru Gothic",sans-serif;font-size:50px;font-weight:900;line-height:1;white-space:nowrap}
.date-box .dow{display:inline-block;width:28px;height:28px;border-radius:50%;background:var(--red);color:#fff;
  font-size:16px;line-height:28px;vertical-align:middle;margin-left:3px}
.date-box .time{font-size:19px;font-weight:700;color:var(--ink);margin-top:4px}
.date-box .time small{display:block;font-size:12px;font-weight:400}

.phone{position:absolute;left:40px;top:1000px;display:flex;align-items:center;gap:12px;color:var(--red)}
.phone svg{width:46px;height:46px}
.phone span{font-size:56px;font-weight:900;letter-spacing:.02em;line-height:1}
.phone-note{position:absolute;left:100px;top:1064px;font-size:12px;color:var(--muted)}

.footer{position:absolute;left:0;top:1110px;width:848px;height:90px;background:var(--pale-green);
  display:flex;align-items:center;justify-content:center;gap:14px;white-space:nowrap}
.footer .org-small{font-size:13px;color:var(--muted)}
.footer .org{font-size:24px;font-weight:700}
.footer .org-brand{font-size:24px;font-weight:700;color:var(--green)}
.footer .contact{font-size:11px;color:var(--muted);margin-left:12px}
</style>
</head>
<body>
<main class="flyer">
  <div class="hero-photo" role="img" aria-label="住宅の模型と設計図面、電卓の写真"></div>
  <div class="hero-fade"></div>

  <div class="brand-box"><span class="brand-dot"></span><span class="brand-name">もえぎうた</span></div>
  <div class="bubble">もえぎうた</div>
  <div class="url-tag">moegiuta.or.jp</div>

  <div class="seminar-tag"><small>セミナー</small><strong>暮らしの「学び場」</strong></div>

  <div class="intro">
    <p>家を建てる前に知っておきたい、資金と土地のこと。多くの方が家づくりの途中で悩み、後悔を感じています。</p>
    <p>このセミナーでは、<span class="accent">家づくりの正しい順番</span>と、はじめに準備すべきことをわかりやすくお伝えします。</p>
    <p>「何から始めればいいの？」そんな疑問をお持ちの方、ぜひお気軽にご参加ください。</p>
    <p>小さなお子様連れの方も安心してご参加いただけます。</p>
  </div>

  <div class="family-art" role="img" aria-label="家族と家のイラスト"></div>

  <div class="badge badge-kids">お子様<br>同伴OK</div>
  <div class="badge badge-free">参加費<br><b>無料</b></div>

  <h1 class="title">「家づくり」はじめの一歩</h1>
  <p class="subtitle">〜後悔しないために学ぶ２つの準備〜</p>

  <ul class="points">
    <li class="lead">当協会認定講師がわかりやすく説明します！</li>
    <li>自分のライフプランを知ることの大切さ</li>
    <li>住宅ローンを組む前に知っておくこと</li>
    <li>土地を買う前に必要なこと</li>
    <li>図面を書く前に必要なこと</li>
    <li>見積もりをする前に必要なこと</li>
    <li>自分の「住宅予算」に自信がもてる</li>
  </ul>

  <div class="promise">「家づくり」はじめの一歩がしっかりできることを<br>盛りだくさんでお話しします！ <em>約90分!!</em></div>

  <section class="details">
    <dl>
      <dt>料金</dt><dd>無料</dd>
      <dt>場所</dt><dd>若葉の家 <small>（緑野市桜町2丁目15番地）</small></dd>
      <dt>講師</dt><dd>もえぎうた認定講師</dd>
      <dt>定員</dt><dd>先着10名</dd>
      <dt>申し込み</dt><dd>お電話にてお申し込みください</dd>
    </dl>
  </section>

  <div class="date-box">
    <div class="label">開催日時</div>
    <div class="year">2020</div>
    <div class="day">3/14<span class="dow">土</span></div>
    <div class="time">13:30〜15:00<small>（受付 13:00〜）</small></div>
  </div>

  <div class="phone">
    <svg viewBox="0 0 24 24" aria-hidden="true"><circle cx="12" cy="12" r="12" fill="#c8323a"/><path d="M8.5 6.5l2 2-1.2 1.6a7 7 0 003.6 3.6l1.6-1.2 2 2-1.4 1.6c-4.2-.4-7.6-3.8-8-8z" fill="#fff"/></svg>
    <span>0120-555-284</span>
  </div>
  <p class="phone-note">受付時間 平日 10:00〜17:00</p>

  <footer class="footer">
    <span class="org-small">一般社団法人</span>
    <span class="org">暮らし応援推進機構</span>
    <span class="org-brand">もえぎうた</span>
    <span class="contact">TEL 000-555-0142 / FAX 000-555-0143</span>
  </footer>
</main>
</body>
</html>
```